Web design

We need the design for the logo and website for a women fashion website. No coding required. The colors used should be neutral (maybe with a light touch of color), the style should be modern, slightly luxurious, not too crowded. The target market is young professionals who love trendy clothes.

Target Market(s)

Young professionals

Industry/Entity Type

Apparel

Number of Pages Required

5+ page

Font styles to use
Sans Serif
Other font styles liked:
• Montserrat, Engravers Gothic, Benton Sans, gotham-book

Colors

Designer to choose colors to be used in the design.

```html
<!DOCTYPE html>
<html lang="en">
<head>
<meta charset="utf-8">
<title>VELLE — Account, Checkout and Shipping Pages</title>
<link rel="stylesheet" href="https://fonts.googleapis.com/css2?family=Montserrat:wght@500;600&family=Roboto:ital,wght@0,300;0,400;0,500;0,700;1,300;1,400&display=swap">
<style>
:root{
  --canvas:#ffffff;
  --board:#f4ece9;
  --footer:#eee2dc;
  --ink:#231f2a;
  --text:#2e2a30;
  --muted:#8a807d;
  --fine:#5b5456;
  --rule:#3b3537;
  --rule-soft:#8f8784;
  --step:#ecdccf;
  --step-on:#e1cdb9;
  --step-line:#e2d2c6;
  --button:#e7dedb;
  --black:#0d0d0d;
  --flag-blue:#203f8c;
  --flag-red:#d5202f;
}
*{box-sizing:border-box}
html,body{margin:0;padding:0}
body{width:1200px;height:959px;overflow:hidden;background:var(--canvas);font-family:"Roboto",Arial,sans-serif;color:var(--text)}
.stage{position:relative;width:2140px;height:1711px;transform:scale(.56075);transform-origin:0 0}

.board{position:absolute;background:var(--board);overflow:hidden}
.board > *, .site-header > *, .site-footer > *, .order-row > *{position:absolute;margin:0}

/* header */
.site-header{left:0;top:0;width:738px;height:130px}
.site-header--compact{transform:scale(.6);transform-origin:0 0}
.nav-link{top:58px;font-size:8.5px;color:var(--text);white-space:nowrap}
.dropdown{left:97px;top:70px;width:73px;height:51px;background:#efe6e2}
.dropdown span{position:absolute;left:6px;font-size:8px;white-space:nowrap}
.dropdown .search{left:3px;top:36px;width:67px;height:9px;background:#e4d7d1;color:var(--muted);font-size:7px;line-height:9px;padding-left:4px}
.brand{left:310px;top:30px;width:200px;height:70px;text-align:center}
.brand-name{position:absolute;left:0;top:34px;width:200px;font-family:"Montserrat",Arial,sans-serif;font-weight:600;font-size:34px;letter-spacing:3px;color:var(--ink);line-height:36px}
.account-link{left:496px;top:58px;width:90px;text-align:right;font-size:8.5px;white-space:nowrap}
.header-icon{top:52px;width:22px;height:22px}
.header-divider{left:621px;top:52px;width:1px;height:22px;background:var(--rule)}

/* steps */
.steps{height:32px}
.step-line{position:absolute;top:15px;height:1px;background:var(--step-line)}
.step{position:absolute;top:0;width:30px;height:30px;border-radius:50%;background:var(--step);color:#c9b8ac;font-size:14px;text-align:center;line-height:30px;font-family:"Roboto",sans-serif}
.step--on{background:var(--step-on);color:var(--ink);font-weight:500}
.steps--small .step{width:16px;height:16px;line-height:16px;font-size:7px}
.steps--small .step-line{top:8px}

/* forms */
.page-title{font-family:"Montserrat",Arial,sans-serif;font-weight:500;color:var(--ink)}
.section-title{font-size:15px;font-weight:500;color:var(--ink);white-space:nowrap}
.field{border-bottom:1px solid var(--rule);font-size:11px;padding-bottom:2px;line-height:13px}
.social-button{height:24px;background:var(--button);font-size:11px;line-height:24px;text-align:center}
.social-button i{display:inline-block;width:20px;height:20px;border:1px solid var(--rule);border-radius:50%;vertical-align:middle;margin-right:6px;position:relative;top:-1px}
.primary-button{background:var(--black);color:#fff;font-size:10px;text-align:center;line-height:29px;letter-spacing:.3px}

/* footer */
.site-footer{left:0;width:738px;height:181px;background:var(--footer)}
.site-footer--compact{transform:scale(.6);transform-origin:0 0}
.footer-heading{top:36px;font-size:10px;font-weight:500;color:var(--ink);white-space:nowrap}
.footer-heading u{text-underline-offset:2px}
.footer-help{left:65px}
.footer-links{left:65px;top:58px;font-size:10px;line-height:12px}
.footer-legal{left:65px;top:121px;font-size:10px;white-space:nowrap}
.footer-signup{left:476px}
.footer-note{left:476px;top:56px;width:200px;font-size:10px;line-height:12px}
.social-dot{top:115px;width:30px;height:30px;border:1.4px solid var(--rule);border-radius:50%}

/* order table */
.col-head{font-size:11px;top:374px;white-space:nowrap}
.order-row{left:0;width:738px;height:72px}
.product-photo{left:107px;top:0;width:51px;height:71px}
.photo-ivory{background:linear-gradient(180deg,#e8e4df 0%,#f7f5f2 40%,#d9d2cc 65%,#3a2c28 100%)}
.photo-rose{background:linear-gradient(180deg,#ece8e5 0%,#e97aa9 35%,#e56a9e 70%,#f1ecea 100%)}
.product-name{left:174px;top:28px;font-size:12px;line-height:15px;white-space:nowrap}
.cell-rule{top:-8px;width:1px;height:70px;background:var(--rule-soft)}
.qty{left:440px;width:30px;top:37px;text-align:center;font-size:12px}
.price{left:545px;width:60px;top:36px;text-align:center;font-size:13px}

/* payment */
.body-copy{font-size:11px;line-height:13px;width:540px}
.body-copy--italic{font-style:italic}
.pay-name{top:340px;font-family:"Roboto",sans-serif;font-weight:500;font-size:32px;color:var(--ink);letter-spacing:.5px}

/* shipping info */
.ship-title{font-size:8.5px;font-weight:500;color:var(--ink);white-space:nowrap}
.ship-region{font-size:7px;font-weight:700;color:var(--ink);white-space:nowrap}
.fine{font-size:5.6px;line-height:7.4px;width:310px;color:var(--fine)}
.fine--italic{font-style:italic}
.fine--bold{font-weight:700;color:var(--ink)}
.ship-row{left:61px;width:220px}
.ship-cell{position:absolute;top:0;height:100%;border-bottom:.7px solid var(--rule-soft);font-size:5.4px;line-height:7px;color:var(--fine);text-transform:uppercase}
.ship-cell--method{left:0;width:75px}
.ship-cell--time{left:91px;width:47px;white-space:nowrap}
.ship-cell--cost{left:158px;width:47px;white-space:nowrap}
.ship-head .ship-cell{color:var(--ink);white-space:nowrap}
.ship-cell small{display:block;text-transform:none;font-size:5px;line-height:6.5px;margin-top:3px}
</style>
</head>
<body>
<div class="stage">

<!-- Log in -->
<section class="board" style="left:0;top:64px;width:738px;height:653px" aria-label="Log in page">
  <header class="site-header">
    <a class="nav-link" style="left:35px">Latest arrivals</a>
    <a class="nav-link" style="left:97px">Clothes</a>
    <div class="dropdown"><span style="top:8px">Clothes categories</span><span style="top:24px">Sale followed</span><span class="search">search</span></div>
    <a class="nav-link" style="left:178px">Shoes</a>
    <a class="nav-link" style="left:215px">Jewels</a>
    <a class="nav-link" style="left:254px">Accessories</a>
    <div class="brand"><span class="brand-name">VELLE</span></div>
    <a class="account-link">My account</a>
    <svg class="header-icon" style="left:590px" viewBox="0 0 22 22" fill="none" stroke="#231f2a" stroke-width="1.4"><circle cx="11" cy="11" r="10"/><circle cx="11" cy="8.5" r="3.6"/><path d="M4.5 18c1.4-3 4-4.4 6.5-4.4s5.1 1.4 6.5 4.4"/></svg>
    <span class="header-divider"></span>
    <svg class="header-icon" style="left:627px" viewBox="0 0 22 22" fill="none" stroke="#231f2a" stroke-width="1.4"><path d="M11 19s-8-5-8-10.5C3 5.5 5.2 3.5 7.6 3.5c1.5 0 2.7.8 3.4 2 .7-1.2 1.9-2 3.4-2 2.4 0 4.6 2 4.6 5C19 14 11 19 11 19z"/></svg>
    <svg class="header-icon" style="left:653px" viewBox="0 0 22 22" fill="none" stroke="#231f2a" stroke-width="1.4"><path d="M2 8h18l-2 11H4z"/><path d="M6 8l5-5 5 5M7 11v6M11 11v6M15 11v6"/></svg>
    <svg class="header-icon" style="left:684px" viewBox="0 0 22 22"><circle cx="11" cy="11" r="9" fill="#203f8c"/><path d="M3 11h16M11 2v18" stroke="#fff" stroke-width="4"/><path d="M3 11h16M11 2v18" stroke="#d5202f" stroke-width="2"/></svg>
  </header>

  <h1 class="page-title" style="left:296px;top:170px;width:200px;text-align:center;font-size:24px">Log In</h1>
  <p style="left:246px;top:203px;width:300px;text-align:center;font-size:11px">Welcome back babe. Sign in for a faster checkout.</p>
  <div class="field" style="left:268px;top:240px;width:238px">Email address</div>
  <div class="field" style="left:268px;top:289px;width:238px">Password</div>
  <a style="left:268px;top:313px;font-size:10.5px;color:var(--muted)">Forgot your password?</a>
  <div class="social-button" style="left:268px;top:349px;width:117px"><i></i>Friendly</div>
  <div class="social-button" style="left:388px;top:349px;width:118px"><i></i>Quester</div>
  <div class="primary-button" style="left:268px;top:389px;width:238px;height:29px">SIGN IN</div>
  <a style="left:336px;top:437px;width:100px;text-align:center;font-size:10.5px;color:var(--muted);text-decoration:underline;text-underline-offset:3px">Create Account</a>

  <footer class="site-footer" style="top:477px;height:176px">
    <h3 class="footer-heading footer-help"><u>Help</u></h3>
    <p class="footer-links">Email Address<br>Returns/exchanges<br>Delivery Information<br>Faq</p>
    <p class="footer-legal">Terms &amp; Conditions, Privacy Policy and @2021 followed by company name</p>
    <h3 class="footer-heading footer-signup"><u>Sign</u> up for Lumen updates</h3>
    <p class="footer-note">Subscribe to the newsletter to receive up-dates about collections, events, campaigns and special projects</p>
    <span class="social-dot" style="left:475px" aria-label="Video channel"></span>
    <span class="social-dot" style="left:512px" aria-label="Short posts"></span>
    <span class="social-dot" style="left:549px" aria-label="Photo feed"></span>
    <span class="social-dot" style="left:585px" aria-label="Community page"></span>
  </footer>
</section>

<!-- Payment -->
<section class="board" style="left:0;top:816px;width:737px;height:587px" aria-label="Payment page">
  <header class="site-header">
    <a class="nav-link" style="left:35px">Latest arrivals</a>
    <a class="nav-link" style="left:97px">Clothes</a>
    <div class="dropdown"><span style="top:8px">Clothes categories</span><span style="top:24px">Sale followed</span><span class="search">search</span></div>
    <a class="nav-link" style="left:178px">Shoes</a>
    <a class="nav-link" style="left:215px">Jewels</a>
    <a class="nav-link" style="left:254px">Accessories</a>
    <div class="brand"><span class="brand-name">VELLE</span></div>
    <a class="account-link">My account</a>
    <svg class="header-icon" style="left:590px" viewBox="0 0 22 22" fill="none" stroke="#231f2a" stroke-width="1.4"><circle cx="11" cy="11" r="10"/><circle cx="11" cy="8.5" r="3.6"/><path d="M4.5 18c1.4-3 4-4.4 6.5-4.4s5.1 1.4 6.5 4.4"/></svg>
    <span class="header-divider"></span>
    <svg class="header-icon" style="left:627px" viewBox="0 0 22 22" fill="none" stroke="#231f2a" stroke-width="1.4"><path d="M11 19s-8-5-8-10.5C3 5.5 5.2 3.5 7.6 3.5c1.5 0 2.7.8 3.4 2 .7-1.2 1.9-2 3.4-2 2.4 0 4.6 2 4.6 5C19 14 11 19 11 19z"/></svg>
    <svg class="header-icon" style="left:653px" viewBox="0 0 22 22" fill="none" stroke="#231f2a" stroke-width="1.4"><path d="M2 8h18l-2 11H4z"/><path d="M6 8l5-5 5 5M7 11v6M11 11v6M15 11v6"/></svg>
    <svg class="header-icon" style="left:684px" viewBox="0 0 22 22"><circle cx="11" cy="11" r="9" fill="#203f8c"/><path d="M3 11h16M11 2v18" stroke="#fff" stroke-width="4"/><path d="M3 11h16M11 2v18" stroke="#d5202f" stroke-width="2"/></svg>
  </header>

  <div class="steps" style="left:196px;top:141px;width:362px">
    <span class="step-line" style="left:30px;width:305px"></span>
    <span class="step" style="left:0">1</span>
    <span class="step" style="left:165px">2</span>
    <span class="step step--on" style="left:331px">3</span>
  </div>
  <h2 class="section-title" style="left:103px;top:183px">Payment page</h2>
  <p class="body-copy" style="left:103px;top:218px">All orders are dispatched within 2 business days.</p>
  <p class="body-copy body-copy--italic" style="left:103px;top:244px">There may be slight dispatch delays during our Mid Season Sale promotion. Please allow up to an additional 48 hours for dispatch. We thank you for your patience.</p>
  <p class="body-copy body-copy--italic" style="left:103px;top:283px">Note: Due to the current on-going lockdown restrictions in NSW, Australia. Our delivery partners are experiencing some delays and therefore these delivery times may vary. Thank you for your patience during this time.</p>
  <span class="pay-name" style="left:103px">Coinwell</span>
  <span class="pay-name" style="left:266px">Tallypay</span>

  <footer class="site-footer" style="top:406px">
    <h3 class="footer-heading footer-help"><u>Help</u></h3>
    <p class="footer-links">Email Address<br>Returns/exchanges<br>Delivery Information<br>Faq</p>
    <p class="footer-legal">Terms &amp; Conditions, Privacy Policy and @2021 followed by company name</p>
    <h3 class="footer-heading footer-signup"><u>Sign</u> up for Lumen updates</h3>
    <p class="footer-note">Subscribe to the newsletter to receive up-dates about collections, events, campaigns and special projects</p>
    <span class="social-dot" style="left:475px" aria-label="Video channel"></span>
    <span class="social-dot" style="left:512px" aria-label="Short posts"></span>
    <span class="social-dot" style="left:549px" aria-label="Photo feed"></span>
    <span class="social-dot" style="left:585px" aria-label="Community page"></span>
  </footer>
</section>

<!-- Personal information -->
<section class="board" style="left:789px;top:64px;width:738px;height:1062px" aria-label="Personal information page">
  <header class="site-header">
    <a class="nav-link" style="left:35px">Latest arrivals</a>
    <a class="nav-link" style="left:97px">Clothes</a>
    <div class="dropdown"><span style="top:8px">Clothes categories</span><span style="top:24px">Sale followed</span><span class="search">search</span></div>
    <a class="nav-link" style="left:178px">Shoes</a>
    <a class="nav-link" style="left:215px">Jewels</a>
    <a class="nav-link" style="left:254px">Accessories</a>
    <div class="brand"><span class="brand-name">VELLE</span></div>
    <a class="account-link">My account</a>
    <svg class="header-icon" style="left:590px" viewBox="0 0 22 22" fill="none" stroke="#231f2a" stroke-width="1.4"><circle cx="11" cy="11" r="10"/><circle cx="11" cy="8.5" r="3.6"/><path d="M4.5 18c1.4-3 4-4.4 6.5-4.4s5.1 1.4 6.5 4.4"/></svg>
    <span class="header-divider"></span>
    <svg class="header-icon" style="left:627px" viewBox="0 0 22 22" fill="none" stroke="#231f2a" stroke-width="1.4"><path d="M11 19s-8-5-8-10.5C3 5.5 5.2 3.5 7.6 3.5c1.5 0 2.7.8 3.4 2 .7-1.2 1.9-2 3.4-2 2.4 0 4.6 2 4.6 5C19 14 11 19 11 19z"/></svg>
    <svg class="header-icon" style="left:653px" viewBox="0 0 22 22" fill="none" stroke="#231f2a" stroke-width="1.4"><path d="M2 8h18l-2 11H4z"/><path d="M6 8l5-5 5 5M7 11v6M11 11v6M15 11v6"/></svg>
    <svg class="header-icon" style="left:684px" viewBox="0 0 22 22"><circle cx="11" cy="11" r="9" fill="#203f8c"/><path d="M3 11h16M11 2v18" stroke="#fff" stroke-width="4"/><path d="M3 11h16M11 2v18" stroke="#d5202f" stroke-width="2"/></svg>
  </header>

  <div class="steps" style="left:180px;top:141px;width:362px">
    <span class="step-line" style="left:30px;width:305px"></span>
    <span class="step step--on" style="left:0">1</span>
    <span class="step" style="left:166px">2</span>
    <span class="step" style="left:331px">3</span>
  </div>
  <h2 class="section-title" style="left:104px;top:184px">Personal information</h2>
  <div class="field" style="left:107px;top:226px;width:237px">Name</div>
  <div class="field" style="left:369px;top:229px;width:238px">Phone</div>
  <div class="field" style="left:107px;top:265px;width:508px">Delivery Addresses</div>
  <div class="field" style="left:107px;top:300px;width:237px">&nbsp;City</div>
  <div class="field" style="left:369px;top:300px;width:140px">Country</div>

  <h2 class="section-title" style="left:104px;top:345px">Order History</h2>
  <span class="col-head" style="left:104px">The Product</span>
  <span class="col-head" style="left:423px;width:60px;text-align:center">Quantity</span>
  <span class="col-head" style="left:544px;width:70px;text-align:center">Into Money</span>

  <div class="order-row" style="top:396px">
    <div class="product-photo photo-ivory" role="img" aria-label="Model wearing the white ribbed cami midi dress"></div>
    <p class="product-name">Mirela<br>Ribbed Cami Midi Dress - White</p>
    <span class="cell-rule" style="left:393px"></span><span class="cell-rule" style="left:519px"></span>
    <span class="qty">1</span><span class="price">$75</span>
  </div>
  <div class="order-row" style="top:497px">
    <div class="product-photo photo-rose" role="img" aria-label="Model wearing a pink tailored suit"></div>
    <p class="product-name">Mirela<br>Ribbed Cami Midi Dress - White</p>
    <span class="cell-rule" style="left:393px"></span><span class="cell-rule" style="left:519px"></span>
    <span class="qty">1</span><span class="price">$105</span>
  </div>
  <div class="order-row" style="top:607px">
    <div class="product-photo photo-rose" role="img" aria-label="Model wearing a pink tailored suit"></div>
    <p class="product-name">Mirela<br>Ribbed Cami Midi Dress - White</p>
    <span class="cell-rule" style="left:393px"></span><span class="cell-rule" style="left:519px"></span>
    <span class="qty">1</span><span class="price">$105</span>
  </div>
  <div class="order-row" style="top:718px">
    <div class="product-photo photo-ivory" role="img" aria-label="Model wearing the white ribbed cami midi dress"></div>
    <p class="product-name">Mirela<br>Ribbed Cami Midi Dress - White</p>
    <span class="cell-rule" style="left:393px"></span><span class="cell-rule" style="left:519px"></span>
    <span class="qty">1</span><span class="price">$75</span>
  </div>

  <span style="left:107px;top:825px;width:412px;height:1px;background:var(--rule-soft)"></span>
  <span style="left:415px;top:808px;width:100px;text-align:right;font-size:12px">Total Money</span>
  <strong style="left:535px;top:807px;width:80px;text-align:center;font-size:20px;font-weight:700;color:var(--ink)">$480</strong>
  <p style="left:104px;top:833px;font-size:10.5px;font-style:italic;white-space:nowrap">Lorem ipsum dolor sit amet, consectetuer adipiscing elit, sed diam nonum</p>

  <footer class="site-footer" style="top:886px;height:176px">
    <h3 class="footer-heading footer-help"><u>Help</u></h3>
    <p class="footer-links">Email Address<br>Returns/exchanges<br>Delivery Information<br>Faq</p>
    <p class="footer-legal">Terms &amp; Conditions, Privacy Policy and @2021 followed by company name</p>
    <h3 class="footer-heading footer-signup"><u>Sign</u> up for Lumen updates</h3>
    <p class="footer-note">Subscribe to the newsletter to receive up-dates about collections, events, campaigns and special projects</p>
    <span class="social-dot" style="left:475px" aria-label="Video channel"></span>
    <span class="social-dot" style="left:512px" aria-label="Short posts"></span>
    <span class="social-dot" style="left:549px" aria-label="Photo feed"></span>
    <span class="social-dot" style="left:585px" aria-label="Community page"></span>
  </footer>
</section>

<!-- Shipping information -->
<section class="board" style="left:1591px;top:64px;width:442px;height:1619px" aria-label="Shipping information page">
  <header class="site-header site-header--compact">
    <a class="nav-link" style="left:35px">Latest arrivals</a>
    <a class="nav-link" style="left:97px">Clothes</a>
    <div class="dropdown"><span style="top:8px">Clothes categories</span><span style="top:24px">Sale followed</span><span class="search">search</span></div>
    <a class="nav-link" style="left:178px">Shoes</a>
    <a class="nav-link" style="left:215px">Jewels</a>
    <a class="nav-link" style="left:254px">Accessories</a>
    <div class="brand"><span class="brand-name">VELLE</span></div>
    <a class="account-link">My account</a>
    <svg class="header-icon" style="left:590px" viewBox="0 0 22 22" fill="none" stroke="#231f2a" stroke-width="1.4"><circle cx="11" cy="11" r="10"/><circle cx="11" cy="8.5" r="3.6"/><path d="M4.5 18c1.4-3 4-4.4 6.5-4.4s5.1 1.4 6.5 4.4"/></svg>
    <span class="header-divider"></span>
    <svg class="header-icon" style="left:627px" viewBox="0 0 22 22" fill="none" stroke="#231f2a" stroke-width="1.4"><path d="M11 19s-8-5-8-10.5C3 5.5 5.2 3.5 7.6 3.5c1.5 0 2.7.8 3.4 2 .7-1.2 1.9-2 3.4-2 2.4 0 4.6 2 4.6 5C19 14 11 19 11 19z"/></svg>
    <svg class="header-icon" style="left:653px" viewBox="0 0 22 22" fill="none" stroke="#231f2a" stroke-width="1.4"><path d="M2 8h18l-2 11H4z"/><path d="M6 8l5-5 5 5M7 11v6M11 11v6M15 11v6"/></svg>
    <svg class="header-icon" style="left:684px" viewBox="0 0 22 22"><circle cx="11" cy="11" r="9" fill="#203f8c"/><path d="M3 11h16M11 2v18" stroke="#fff" stroke-width="4"/><path d="M3 11h16M11 2v18" stroke="#d5202f" stroke-width="2"/></svg>
  </header>

  <div class="steps steps--small" style="left:112px;top:85px;width:215px">
    <span class="step-line" style="left:16px;width:183px"></span>
    <span class="step" style="left:0">1</span>
    <span class="step step--on" style="left:99px">2</span>
    <span class="step" style="left:198px">3</span>
  </div>

  <h2 class="ship-title" style="left:61px;top:109px">Shipping Information</h2>
  <p class="fine" style="left:61px;top:130px">All orders are dispatched within 2 business days.</p>
  <p class="fine fine--italic" style="left:61px;top:146px">There may be slight dispatch delays during our Mid Season Sale promotion. Please allow up to an additional 48 hours for dispatch. We thank you for your patience.</p>
  <p class="fine fine--italic" style="left:61px;top:169px">Note: Due to the current on-going lockdown restrictions in NSW, Australia. Our delivery partners are experiencing some delays and therefore these delivery times may vary. Thank you for your patience during this time.</p>

  <h3 class="ship-region" style="left:61px;top:198px">AUSTRALIA</h3>
  <p class="fine fine--bold" style="left:61px;top:214px">Coastline Post are currently experiencing an additional 2-3 day delay with deliveries to Victoria, we apologise for any inconvenience.</p>
  <div class="ship-row ship-head" style="top:239px;height:9px"><span class="ship-cell ship-cell--method">Shipping method</span><span class="ship-cell ship-cell--time">Delivery time*</span><span class="ship-cell ship-cell--cost">Delivery cost</span></div>
  <div class="ship-row" style="top:256px;height:42px"><span class="ship-cell ship-cell--method">Same day afternoon delivery<small>Orders placed after 10am are sent the next business day</small></span><span class="ship-cell ship-cell--time" style="padding-top:14px">1PM - 6PM</span><span class="ship-cell ship-cell--cost" style="padding-top:14px">$14.99AUD</span></div>
  <div class="ship-row" style="top:308px;height:42px"><span class="ship-cell ship-cell--method">Same day evening delivery<small>Orders placed after 2pm are sent the next business day</small></span><span class="ship-cell ship-cell--time" style="padding-top:14px">6PM - 9PM</span><span class="ship-cell ship-cell--cost" style="padding-top:14px">$14.99AUD</span></div>
  <div class="ship-row" style="top:362px;height:26px"><span class="ship-cell ship-cell--method">Express</span><span class="ship-cell ship-cell--time">1 - 3 days*</span><span class="ship-cell ship-cell--cost">$10.50AUD<br><br>Free over $100AUD</span></div>
  <div class="ship-row" style="top:398px;height:26px"><span class="ship-cell ship-cell--method">Standard</span><span class="ship-cell ship-cell--time">2 - 10 days</span><span class="ship-cell ship-cell--cost">$7.99AUD<br><br>Free over $100AUD</span></div>
  <p class="fine" style="left:61px;top:435px;width:325px">*Same Day and Twilight Delivery is only available in selected NSW areas. Enter your postcode at checkout to check availability. Authority to leave applies and it is only offered to residential and business addresses. <b>PO Boxes and Parcel Lockers will be returned to sender.</b> If the driver cannot leave the parcel in a safe place, delivery is tried again the next business day. If a business address is closed, the parcel is returned to sender. Not available on weekends, public holidays, Christmas Eve and New Years Eve.</p>
  <p class="fine" style="left:61px;top:481px;width:325px">* We use Coastline Post Express, which is next business day delivery within the express network in Australian capital cities, major metro areas and Perth CBD. Check if your postcode is eligible here. For other WA and NT areas, express can take up to 3 business days.</p>

  <h3 class="ship-region" style="left:61px;top:522px">NEW ZEALAND</h3>
  <div class="ship-row ship-head" style="top:538px;height:9px"><span class="ship-cell ship-cell--method">Shipping method</span><span class="ship-cell ship-cell--time">Delivery time*</span><span class="ship-cell ship-cell--cost">Delivery cost</span></div>
  <div class="ship-row" style="top:557px;height:26px"><span class="ship-cell ship-cell--method">Express</span><span class="ship-cell ship-cell--time">1 - 3 days*</span><span class="ship-cell ship-cell--cost">$15<br><br>Free over $300</span></div>
  <div class="ship-row" style="top:593px;height:27px"><span class="ship-cell ship-cell--method">Standard</span><span class="ship-cell ship-cell--time">3 - 8 days</span><span class="ship-cell ship-cell--cost">$10<br><br>Free over $100</span></div>

  <h3 class="ship-region" style="left:61px;top:651px">UNITED STATES</h3>
  <div class="ship-row ship-head" style="top:667px;height:9px"><span class="ship-cell ship-cell--method">Shipping method</span><span class="ship-cell ship-cell--time">Delivery time*</span><span class="ship-cell ship-cell--cost">Delivery cost</span></div>
  <div class="ship-row" style="top:685px;height:27px"><span class="ship-cell ship-cell--method">Standard</span><span class="ship-cell ship-cell--time">4 - 10 days</span><span class="ship-cell ship-cell--cost">$9.99USD<br><br>Free over $130USD</span></div>
  <div class="ship-row" style="top:722px;height:14px"><span class="ship-cell ship-cell--method">Express</span><span class="ship-cell ship-cell--time">2 - 5 days</span><span class="ship-cell ship-cell--cost">$35USD</span></div>

  <h3 class="ship-region" style="left:61px;top:765px">CANADA</h3>
  <div class="ship-row ship-head" style="top:782px;height:9px"><span class="ship-cell ship-cell--method">Shipping method</span><span class="ship-cell ship-cell--time">Delivery time*</span><span class="ship-cell ship-cell--cost">Delivery cost</span></div>
  <div class="ship-row" style="top:801px;height:15px"><span class="ship-cell ship-cell--method">Express</span><span class="ship-cell ship-cell--time">2 - 4 days</span><span class="ship-cell ship-cell--cost">$19.99USD</span></div>

  <div class="ship-row ship-head" style="top:861px;height:9px"><span class="ship-cell ship-cell--method">Shipping method</span><span class="ship-cell ship-cell--time">Delivery time*</span><span class="ship-cell ship-cell--cost">Delivery cost</span></div>
  <div class="ship-row" style="top:879px;height:27px"><span class="ship-cell ship-cell--method">Standard</span><span class="ship-cell ship-cell--time">4 - 10 days</span><span class="ship-cell ship-cell--cost">$9.99USD<br><br>Free over $130USD</span></div>
  <div class="ship-row" style="top:916px;height:15px"><span class="ship-cell ship-cell--method">Express</span><span class="ship-cell ship-cell--time">2 - 4 days</span><span class="ship-cell ship-cell--cost">$35USD</span></div>

  <h3 class="ship-region" style="left:61px;top:960px">EUROPE</h3>
  <div class="ship-row ship-head" style="top:976px;height:9px"><span class="ship-cell ship-cell--method">Shipping method</span><span class="ship-cell ship-cell--time">Delivery time*</span><span class="ship-cell ship-cell--cost">Delivery cost</span></div>
  <div class="ship-row" style="top:994px;height:27px"><span class="ship-cell ship-cell--method">Standard</span><span class="ship-cell ship-cell--time">7 - 12 days</span><span class="ship-cell ship-cell--cost">$9.99USD<br><br>Free over $130USD</span></div>
  <div class="ship-row" style="top:1031px;height:14px"><span class="ship-cell ship-cell--method">Express</span><span class="ship-cell ship-cell--time">2 - 4 days</span><span class="ship-cell ship-cell--cost">$35USD</span></div>
  <p class="fine fine--italic" style="left:61px;top:1050px">(Selected European countries standard shipping will be calculated at checkout)</p>

  <h3 class="ship-region" style="left:61px;top:1087px">ROW</h3>
  <div class="ship-row ship-head" style="top:1103px;height:9px"><span class="ship-cell ship-cell--method">Shipping method</span><span class="ship-cell ship-cell--time">Delivery time*</span><span class="ship-cell ship-cell--cost">Delivery cost</span></div>
  <div class="ship-row" style="top:1122px;height:14px"><span class="ship-cell ship-cell--method">Express</span><span class="ship-cell ship-cell--time">2 - 7 days</span><span class="ship-cell ship-cell--cost" style="text-transform:none">Price calculated at checkout</span></div>

  <h3 class="ship-region" style="left:61px;top:1169px">WHAT YOU NEED TO KNOW - AU ORDERS</h3>
  <p class="fine" style="left:61px;top:1184px">Delivery times are stated in business days.</p>
  <p class="fine" style="left:61px;top:1199px">*Please note, Norla is not responsible for delays caused by Coastline Post, especially during busy seasons. These are our best delivery estimates and are usually reliable and quick. Items bought on pre-order follow their own shipping times.</p>
  <p class="fine" style="left:61px;top:1231px">All Coastline Post parcels are sent with authority to leave. You will only be asked to sign if the courier decides there is no safe place for the parcel. If it can be left, the courier will record a proof of delivery instead.</p>
  <p class="fine" style="left:61px;top:1262px">If the receiver lets the courier deliver without a signature, or gives authority to leave, Norla is not liable if the parcel goes missing and cannot refund or resend it. We appreciate your understanding.</p>
  <p class="fine" style="left:61px;top:1293px">If you have any further questions, please get in contact with our customer service team here.</p>

  <h3 class="ship-region" style="left:61px;top:1309px">WHAT YOU NEED TO KNOW - INTERNATIONAL ORDERS</h3>
  <p class="fine" style="left:61px;top:1326px">Delivery is stated in business days, and orders must be placed before 2PM AEST to be dispatched the same day. Orders placed after the cut-off are processed the following business day. Orders placed late on Friday or over the weekend are processed on Monday.</p>
  <p class="fine" style="left:61px;top:1366px">Please note, Norla is not responsible for delays caused by couriers. These may happen from time to time, especially in peak periods. Our delivery estimates are usually reliable and quick. Pre-order items follow their own shipping times.</p>
  <p class="fine" style="left:61px;top:1397px">Taxes are included in the price of the product, so no extra taxes are due at checkout. Some orders may incur duties if the total value goes over a limit set by the destination country. In that case the courier will contact you before the parcel is released to you.</p>
  <p class="fine" style="left:61px;top:1436px">If a parcel is not claimed or is refused by the receiver, Swiftline will attempt a new delivery. If Swiftline and our team cannot arrange it within the courier's holding time, the parcel may be returned or abandoned by local authorities, and no refund will be given.</p>
  <p class="fine" style="left:61px;top:1475px">*All our Express International orders are shipped via Swiftline Express.</p>
  <p class="fine" style="left:61px;top:1491px">We do not currently ship orders to PO or APO boxes via international postage at this time.</p>

  <footer class="site-footer site-footer--compact" style="top:1514px;height:176px">
    <h3 class="footer-heading footer-help"><u>Help</u></h3>
    <p class="footer-links">Email Address<br>Returns/exchanges<br>Delivery Information<br>Faq</p>
    <p class="footer-legal">Terms &amp; Conditions, Privacy Policy and @2021 followed by company name</p>
    <h3 class="footer-heading footer-signup"><u>Sign</u> up for Lumen updates</h3>
    <p class="footer-note" style="width:180px">Subscribe to the newsletter to receive updates about collections, events, campaigns and special projects</p>
    <span class="social-dot" style="left:475px" aria-label="Video channel"></span>
    <span class="social-dot" style="left:512px" aria-label="Short posts"></span>
    <span class="social-dot" style="left:549px" aria-label="Photo feed"></span>
    <span class="social-dot" style="left:585px" aria-label="Community page"></span>
  </footer>
</section>

</div>
</body>
</html>
```